New Label Design Project for Tinkers den wines

I would like to purchase a customized version of a design you have previously submitted - https://www.artmarketfolio.com.au/design/57302946

We need a label that that we can use for our new vintage shiraz, Merlot and Pinot Noir products. This Label will be just 1 label that will be front and back label.
Please see attached

Target Market(s)

young and old wine drinkers

Industry/Entity Type

Wine

Colors

Designer to choose colors to be used in the design.

Requirements
Must have
• logo but also is a bit funky
Nice to have
• mixture of Funky and Modern

```html
<!DOCTYPE html>
<html lang="en">
<head>
<meta charset="UTF-8">
<title>Tinker's Den Shiraz – Label Design</title>
<link href="https://fonts.googleapis.com/css2?family=Oswald:wght@400;500&display=swap" rel="stylesheet">
<style>
  :root {
    --stage: #35363b;
    --label-dark: #0c0c0c;
    --label-mid: #1d1d1d;
    --brand-red: #e30613;
    --brand-red-deep: #c70510;
    --ink-white: #ffffff;
    --ink-soft: #d9d9d9;
    --ghost: #2a2a2a;
    --ghost-light: #333333;
    --rule: #3a3a3a;
  }
  * { margin: 0; padding: 0; box-sizing: border-box; }
  html, body {
    width: 1200px;
    height: 900px;
    overflow: hidden;
    background: var(--stage);
  }
  .canvas {
    position: relative;
    width: 1200px;
    height: 900px;
    display: flex;
    align-items: center;
    justify-content: center;
  }
  .label {
    position: relative;
    width: 600px;
    height: 770px;
    background: linear-gradient(180deg, var(--label-dark) 0%, var(--label-mid) 100%);
    overflow: hidden;
    font-family: "Oswald", sans-serif;
    color: var(--ink-white);
  }
  .label__backdrop {
    position: absolute;
    left: 0;
    top: 400px;
    width: 600px;
    height: 340px;
    background: radial-gradient(ellipse at 30% 60%, var(--ghost-light) 0%, var(--ghost) 45%, transparent 75%),
                radial-gradient(ellipse at 78% 55%, var(--ghost-light) 0%, var(--ghost) 40%, transparent 72%);
    opacity: 0.9;
  }
  .label__rule {
    position: absolute;
    left: 0;
    top: 742px;
    width: 600px;
    height: 1px;
    background: var(--rule);
  }
  .brand-band {
    position: absolute;
    left: 174px;
    top: 0;
    width: 280px;
    height: 170px;
    background: var(--brand-red);
  }
  .brand-band__scene {
    position: absolute;
    left: 40px;
    top: 62px;
    width: 200px;
    height: 90px;
    background: linear-gradient(180deg, #f1f1f1 0%, #d8d8d8 100%);
    opacity: 0.92;
  }
  .brand-plate {
    position: absolute;
    left: 160px;
    top: 170px;
    width: 308px;
    height: 100px;
    background: var(--brand-red);
    border-radius: 0 0 40px 40px;
    display: flex;
    align-items: center;
    justify-content: center;
  }
  .brand-name {
    font-family: "Oswald", sans-serif;
    font-weight: 500;
    font-size: 44px;
    letter-spacing: 2px;
    color: var(--ink-white);
  }
  .varietal {
    position: absolute;
    top: 400px;
    width: 100%;
    text-align: center;
    font-weight: 500;
    font-size: 66px;
    line-height: 1;
    letter-spacing: 16px;
    padding-left: 16px;
  }
  .region {
    position: absolute;
    top: 482px;
    width: 100%;
    text-align: center;
    font-weight: 400;
    font-size: 32px;
    line-height: 1;
    letter-spacing: 7px;
    padding-left: 7px;
  }
  .vintage {
    position: absolute;
    left: 280px;
    top: 574px;
    width: 38px;
    height: 64px;
    border: 2px solid var(--brand-red);
    color: var(--brand-red);
    font-size: 26px;
    line-height: 29px;
    text-align: center;
    font-weight: 400;
  }
  .origin {
    position: absolute;
    top: 688px;
    width: 100%;
    text-align: center;
    font-size: 15px;
    letter-spacing: 3px;
    color: var(--ink-soft);
  }
</style>
</head>
<body>
  <main class="canvas">
    <section class="label">
      <div class="label__backdrop" role="img" aria-label="Faint background illustration of a gentleman driving a horse-drawn carriage"></div>
      <div class="label__rule"></div>

      <div class="brand-band">
        <div class="brand-band__scene" role="img" aria-label="White silhouette of a horse pulling a wagon loaded with barrels"></div>
      </div>
      <div class="brand-plate">
        <span class="brand-name">Tinker's Den</span>
      </div>

      <h1 class="varietal">SHIRAZ</h1>
      <p class="region">MT. BENSON</p>
      <div class="vintage">20<br>07</div>
      <p class="origin">WINE OF AUSTRALIA</p>
    </section>
  </main>
</body>
</html>
```